Design a New Business Card for Our Company

We are looking for fresh, unique, and a modern business card that reflects our roots as digital marketing agency focused on SEM.

Industry/Entity Type

Marketing

Contact Information for Business Card

looking for very unique out of the box designs. clean and modern that compliments our logo

Requirements
Must have
• colors should match our logo
• Front should have name, address, email, and phone/fax of the person, phone/fax are the same number
• back should have our url

```html
<!DOCTYPE html>
<html lang="en">
<head>
<meta charset="utf-8">
<title>Northpeak Business Card</title>
<link href="https://fonts.googleapis.com/css2?family=Outfit:wght@300;400;500;600&display=swap" rel="stylesheet">
<style>
  :root {
    --page: #ffffff;
    --card: #252525;
    --band: #b1b1b1;
    --blue: #5b97d2;
    --grey: #b9b9b9;
    --text-light: #d0d0d0;
    --dot: #333333;
  }
  html, body {
    margin: 0;
    padding: 0;
    width: 1200px;
    height: 1000px;
    overflow: hidden;
    background: var(--page);
    font-family: "Outfit", sans-serif;
  }
  .canvas { position: relative; width: 1200px; height: 1000px; }

  .card { position: absolute; width: 557px; background: var(--card); overflow: hidden; }
  .card-front { left: 214px; top: 170px; height: 318px; }
  .card-back { left: 421px; top: 563px; height: 318px; }

  .front-band { position: absolute; left: 0; bottom: 0; width: 100%; height: 16px; background: var(--band); }

  .rule { position: absolute; height: 2px; background: var(--blue); top: 96px; }
  .rule-lead { left: 0; width: 18px; }
  .rule-link { left: 184px; width: 87px; }

  .person-name { position: absolute; left: 34px; top: 79px; margin: 0; font-size: 28px; font-weight: 500; color: var(--blue); line-height: 1; }
  .person-role { position: absolute; left: 34px; top: 118px; margin: 0; font-size: 21px; font-weight: 300; color: var(--text-light); line-height: 1; }

  .brand { position: absolute; display: flex; align-items: center; color: var(--grey); font-weight: 500; line-height: 1; letter-spacing: -0.5px; }
  .brand-dot { border-radius: 50%; background: var(--blue); flex: none; }
  .brand-front { left: 272px; top: 72px; gap: 12px; font-size: 46px; }
  .brand-front .brand-dot { width: 34px; height: 34px; }
  .brand-back { left: 104px; top: 116px; gap: 16px; font-size: 64px; }
  .brand-back .brand-dot { width: 52px; height: 52px; }

  .contact { position: absolute; display: flex; align-items: center; gap: 16px; font-size: 16px; font-weight: 300; color: var(--text-light); line-height: 1.2; }
  .contact-icon { width: 36px; height: 36px; border-radius: 50%; background: var(--blue); display: flex; align-items: center; justify-content: center; flex: none; }
  .contact-icon svg { width: 20px; height: 20px; fill: var(--card); }
  .contact-phone { left: 31px; top: 204px; }
  .contact-fax { left: 31px; top: 245px; }
  .contact-email { left: 273px; top: 204px; gap: 12px; }
  .contact-address { left: 273px; top: 247px; gap: 14px; }

  .dot-pattern { position: absolute; left: 0; top: 0; width: 300px; height: 318px;
    background: radial-gradient(ellipse at 40% 45%, var(--dot) 0%, rgba(51,51,51,0.5) 45%, rgba(37,37,37,0) 80%); }

  .website { position: absolute; left: 0; width: 100%; top: 248px; margin: 0; text-align: center; font-size: 18px; font-weight: 300; letter-spacing: 1px; color: var(--text-light); }
</style>
</head>
<body>
<main class="canvas">

  <section class="card card-front" aria-label="Business card front">
    <div class="rule rule-lead"></div>
    <h1 class="person-name">Ellis Carter</h1>
    <p class="person-role">Director</p>
    <div class="rule rule-link"></div>
    <div class="brand brand-front"><span class="brand-dot"></span><span>Northpeak</span></div>

    <div class="contact contact-phone">
      <span class="contact-icon"><svg viewBox="0 0 24 24"><path d="M6.6 10.8a15.1 15.1 0 0 0 6.6 6.6l2.2-2.2a1 1 0 0 1 1-.25 11.4 11.4 0 0 0 3.6.57 1 1 0 0 1 1 1V20a1 1 0 0 1-1 1A17 17 0 0 1 3 4a1 1 0 0 1 1-1h3.5a1 1 0 0 1 1 1c0 1.25.2 2.45.57 3.57a1 1 0 0 1-.25 1z"/></svg></span>
      <span>0198 765 432</span>
    </div>
    <div class="contact contact-fax">
      <span class="contact-icon"><svg viewBox="0 0 24 24"><path d="M7 3h10v5H7z M4 9h16a1 1 0 0 1 1 1v7h-3v4H6v-4H3v-7a1 1 0 0 1 1-1zm4 6v4h8v-4z"/></svg></span>
      <span>0198 765 432</span>
    </div>
    <div class="contact contact-email">
      <span class="contact-icon"><svg viewBox="0 0 24 24"><path d="M3 6h18v12H3z M3 6l9 7 9-7" stroke="#5b97d2" stroke-width="1.5"/></svg></span>
      <span>Ellis@northpeak.com</span>
    </div>
    <div class="contact contact-address">
      <span class="contact-icon"><svg viewBox="0 0 24 24"><path d="M12 2a7 7 0 0 0-7 7c0 5 7 13 7 13s7-8 7-13a7 7 0 0 0-7-7zm0 9.5A2.5 2.5 0 1 1 12 6.5a2.5 2.5 0 0 1 0 5z"/></svg></span>
      <span>42 Maple Row Ave.<br>Fairview, NY 10560</span>
    </div>

    <div class="front-band"></div>
  </section>

  <section class="card card-back" aria-label="Business card back">
    <div class="dot-pattern" role="img" aria-label="Faint scattered circle pattern in dark grey"></div>
    <div class="brand brand-back"><span class="brand-dot"></span><span>Northpeak</span></div>
    <p class="website">www. Northpeak.com</p>
  </section>

</main>
</body>
</html>
```